house and garden repairs and maintenance, bathroom repairs, painting inside and out, all outdoor lawns and gardens ,landscaping, spraying, lawn mowing cylinder or rotary

Industry/Entity Type

Painting

Contact Information for Business Card

tidy wren home and yard, repairs and maintenance inside and out mark 0427361508 dean 0439682715

Colors

Designer to choose colors to be used in the design.

```html
<!DOCTYPE html>
<html lang="en">
<head>
<meta charset="utf-8">
<title>Tidy Wren Home and Yard – Business Cards</title>
<link rel="stylesheet" href="https://fonts.googleapis.com/css2?family=Cinzel:wght@700&family=Crimson+Text:ital,wght@0,400;0,600;1,400&display=swap">
<style>
  :root {
    --bg: #4a3a44;
    --card: #ffffff;
    --green-dark: #56773a;
    --green-light: #8cc63f;
    --blue: #1f6fb8;
    --tick: #c1272d;
    --ink: #1e1e1e;
    --muted: #555555;
  }
  * { box-sizing: border-box; margin: 0; padding: 0; }
  html, body { width: 1200px; height: 800px; overflow: hidden; }
  body {
    background: var(--bg);
    display: flex;
    align-items: center;
    justify-content: center;
    gap: 40px;
  }
  .card {
    position: relative;
    width: 540px;
    height: 310px;
    background: var(--card);
    overflow: hidden;
    box-shadow: 0 10px 30px rgba(0,0,0,.35);
  }
  .card-shapes { position: absolute; inset: 0; }

  .business {
    position: absolute;
    font-family: "Crimson Text", serif;
  }
  .business-name {
    font-weight: 600;
    font-size: 27px;
    line-height: 1.1;
    color: var(--green-dark);
  }
  .business-tagline {
    font-size: 13.5px;
    line-height: 1.25;
    color: var(--muted);
    margin-top: 8px;
  }

  /* Services card */
  .card--services .business { left: 330px; top: 100px; width: 190px; }
  .service-list {
    position: absolute;
    left: 24px;
    top: 84px;
    width: 296px;
    list-style: none;
    font-family: "Crimson Text", serif;
    font-size: 14px;
    line-height: 1.3;
    color: var(--ink);
  }
  .service-list li { display: flex; align-items: center; gap: 6px; }
  .service-list svg { width: 10px; height: 10px; flex: none; }

  /* Contact card */
  .card--contact .business { left: 262px; top: 128px; width: 260px; }
  .contacts {
    position: absolute;
    left: 30px;
    top: 40px;
    color: #fff;
  }
  .contact + .contact { margin-top: 14px; }
  .contact-name {
    font-family: "Cinzel", serif;
    font-weight: 700;
    font-size: 20px;
    letter-spacing: 1px;
  }
  .contact-phone {
    display: flex; align-items: center; gap: 6px;
    font-family: "Crimson Text", serif;
    font-size: 21px;
  }
  .contact-phone svg { width: 12px; height: 14px; }
</style>
</head>
<body>

  <section class="card card--services" aria-label="Services side">
    <svg class="card-shapes" viewBox="0 0 540 310" aria-hidden="true">
      <path d="M0 0 H230 C150 10 60 30 0 80 Z" fill="var(--green-light)"/>
      <path d="M30 68 C90 30 180 12 260 18" fill="none" stroke="var(--blue)" stroke-width="6"/>
      <path d="M0 234 C140 262 300 270 540 256 V310 H0 Z" fill="var(--green-light)"/>
      <path d="M150 238 C280 256 420 252 540 244" fill="none" stroke="var(--blue)" stroke-width="6"/>
    </svg>

    <ul class="service-list">
      <li><svg viewBox="0 0 10 10"><path d="M1 5 L4 8 L9 2" fill="none" stroke="var(--tick)" stroke-width="2"/></svg>House and garden repairs and maintenance</li>
      <li><svg viewBox="0 0 10 10"><path d="M1 5 L4 8 L9 2" fill="none" stroke="var(--tick)" stroke-width="2"/></svg>Bathroom repairs</li>
      <li><svg viewBox="0 0 10 10"><path d="M1 5 L4 8 L9 2" fill="none" stroke="var(--tick)" stroke-width="2"/></svg>Painting inside and out</li>
      <li><svg viewBox="0 0 10 10"><path d="M1 5 L4 8 L9 2" fill="none" stroke="var(--tick)" stroke-width="2"/></svg>All outdoor lawns and gardens</li>
      <li><svg viewBox="0 0 10 10"><path d="M1 5 L4 8 L9 2" fill="none" stroke="var(--tick)" stroke-width="2"/></svg>Landscaping</li>
      <li><svg viewBox="0 0 10 10"><path d="M1 5 L4 8 L9 2" fill="none" stroke="var(--tick)" stroke-width="2"/></svg>Spraying</li>
      <li><svg viewBox="0 0 10 10"><path d="M1 5 L4 8 L9 2" fill="none" stroke="var(--tick)" stroke-width="2"/></svg>Lawn mowing cylinder or rotary</li>
    </ul>

    <div class="business">
      <p class="business-name">Tidy Wren<br>Home and Yard</p>
      <p class="business-tagline">Repairs and maintenance inside and out</p>
    </div>
  </section>

  <section class="card card--contact" aria-label="Contact side">
    <svg class="card-shapes" viewBox="0 0 540 310" aria-hidden="true">
      <path d="M0 0 H330 C240 40 200 140 215 310 H0 Z" fill="var(--green-dark)"/>
      <path d="M330 0 C250 40 210 140 225 310" fill="none" stroke="var(--green-light)" stroke-width="9"/>
    </svg>

    <div class="contacts">
      <div class="contact">
        <p class="contact-name">Mark</p>
        <p class="contact-phone"><svg viewBox="0 0 12 14"><path d="M3 1 L5 4 L3.5 5.5 C4.5 8 6 9.5 8 10.5 L9.5 9 L12 11 L10 13.5 C5 13 1 8 1 2.5 Z" fill="#fff"/></svg>0427361508</p>
      </div>
      <div class="contact">
        <p class="contact-name">Dean</p>
        <p class="contact-phone"><svg viewBox="0 0 12 14"><path d="M3 1 L5 4 L3.5 5.5 C4.5 8 6 9.5 8 10.5 L9.5 9 L12 11 L10 13.5 C5 13 1 8 1 2.5 Z" fill="#fff"/></svg>0439682715</p>
      </div>
    </div>

    <div class="business">
      <p class="business-name">Tidy Wren Home and Yard</p>
      <p class="business-tagline">Repairs and maintenance inside and out</p>
    </div>
  </section>

</body>
</html>
```